Kestonvale Hawks FC Website

We are looking to develop a new website for Kestonvale FC. Kestonvale FC has now joined with Kestonvale Hawks FC and we are looking at a website that can work for both clubs. Kestonvale FC play in a local park football competition while kestonvale Hawks are a Semi Professional team that plays in the Harbourline Premier Division Competition. What we are after is two separate website off the one platform. I have attached both team logos for you to visualise. Also you can look at the existing kestonvale website www.kestonvalefc.com.au. We are looking for a huge improvement in the website and it will be imperative we have links to sponsors and the sponsors can get regular visuals. Weare looking to move this club forward and have a very professional website that can communicate clearly with the community.

Hi All,

Please remember that the website is to represent two clubs;
1. Kestonvale Hawks FC (Competes in Semi Professional League)
2. Kestonvale FC (Compete in TMCJA League which is a lower level)

Further to this the Kestonvale Hawks FC page will require a player profile page which will show photos of each player and a little bio on each.

Thanks

Reason: Would like to spend more time review existing and new designs

```html
<!DOCTYPE html>
<html lang="en">
<head>
<meta charset="utf-8">
<title>Kestonvale FC</title>
<link rel="stylesheet" href="https://fonts.googleapis.com/css2?family=Exo+2:wght@400;500;600&family=Questrial&family=Arimo:ital,wght@0,400;0,700;1,400&display=swap">
<style>
:root{
  --red:#c4161c;
  --red-dark:#9e0f14;
  --ink:#2b2b2b;
  --grey-text:#8a8a8a;
  --light-bg:#efefef;
  --nav-bg:#fafafa;
  --top-band:#2a2522;
  --yellow:#f2c21b;
  --footer-bg:#1d1d1d;
  --footer-line:#3a3a3a;
  --footer-text:#c9c9c9;
  --white:#ffffff;
}
*{margin:0;padding:0;box-sizing:border-box}
html,body{width:1200px;height:2214px;overflow:hidden;background:var(--white)}
body{position:relative;font-family:"Questrial",sans-serif;color:var(--ink)}
.abs{position:absolute}
ul{list-style:none}

/* header */
.top-band{left:0;top:0;width:1200px;height:37px;background:linear-gradient(#4a413b,var(--top-band))}
.nav-bar{left:0;top:37px;width:1200px;height:55px;background:var(--nav-bg);border-bottom:1px solid #ddd}
.nav-link{top:37px;height:55px;line-height:55px;font-family:"Exo 2",sans-serif;font-size:14px;font-weight:500;color:#222;text-transform:uppercase;letter-spacing:.2px}
.nav-link.active{color:var(--red);border-bottom:3px solid var(--red);left:158px;width:70px;text-align:center}
.brand-tab{left:540px;top:0;width:120px;height:133px;background:var(--white);box-shadow:0 2px 6px rgba(0,0,0,.25);border-radius:0 0 60px 60px;display:flex;flex-direction:column;align-items:center;justify-content:center;z-index:3;font-family:"Exo 2",sans-serif;font-weight:600;color:var(--red);font-size:17px;line-height:1.15;text-align:center}

/* hero */
.hero{left:0;top:92px;width:1200px;height:470px;background:radial-gradient(ellipse at 55% 30%,#d9c7a6 0%,#8d7c62 35%,#4a4c3e 70%,#2c2a25 100%)}
.hero-arrow{width:42px;height:42px;border-radius:50%;border:2px solid var(--white);top:285px}
.hero-arrow.prev{left:63px}
.hero-arrow.next{left:1093px;border-color:var(--red)}
.hero-badge{left:163px;top:336px;width:100px;height:100px;border-radius:50%;background:var(--red)}
.hero-title{left:291px;top:330px;font-family:"Exo 2",sans-serif;font-size:46px;font-weight:500;color:var(--red);letter-spacing:1px}
.hero-text{left:291px;top:384px;width:350px;font-size:14px;line-height:19.5px;color:var(--white)}

/* welcome */
.welcome{left:0;top:562px;width:1200px;height:276px;background:linear-gradient(90deg,#e6e6e6,#f3f3f3 40%,#eeeeee)}
.welcome-title{left:158px;top:600px;font-family:"Exo 2",sans-serif;font-size:45px;line-height:46px;font-weight:400;color:#222}
.welcome-title span{color:var(--red);display:block}
.register-btn{left:158px;top:709px;width:287px;height:86px;background:linear-gradient(#d5222a,var(--red-dark));color:var(--white);padding:14px 0 0 77px;font-family:"Exo 2",sans-serif;box-shadow:0 2px 4px rgba(0,0,0,.3)}
.register-btn .season{font-size:17px;display:block}
.register-btn .cta{font-size:23px;display:block;line-height:28px}
.about-title{left:491px;top:602px;font-family:"Exo 2",sans-serif;font-size:27px;font-weight:400;color:#222;letter-spacing:.5px}
.about-title em{font-style:normal;color:var(--red)}
.about-rule{left:491px;top:649px;width:551px;height:2px;background:#333}
.about-text{left:491px;top:666px;width:551px;font-size:14px;line-height:19.7px;color:var(--grey-text)}

/* fixtures */
.fixtures-title{left:157px;top:888px;font-family:"Exo 2",sans-serif;font-size:33px;font-weight:400;color:var(--red);letter-spacing:.5px}
.fixtures-title span{color:#222}
.fixtures-rule{left:158px;top:942px;width:630px;height:2px;background:#333}
.fixtures-text{left:158px;top:962px;width:615px;font-size:14px;line-height:19.7px;color:var(--grey-text)}
.league-list{top:1057px}
.league-list li{height:26px;line-height:26px;font-family:"Exo 2",sans-serif;font-size:15px;color:#333;padding-left:20px;position:relative;text-transform:uppercase}
.league-list li::before{content:"";position:absolute;left:0;top:9px;width:8px;height:8px;border:1.5px solid #333}
.league-list li.current{color:var(--red)}
.league-list li.current::before{border-color:var(--red)}
.player-photo{left:842px;top:864px;width:200px;height:496px;background:linear-gradient(180deg,#ececec 0%,#b31a22 30%,#a3161d 70%,#e8e8e8 100%);border-radius:60px 60px 10px 10px}

/* no smoking */
.smoke-band{left:0;top:1360px;width:1200px;height:243px;background:linear-gradient(90deg,#e4e4e4,#f1f1f1 45%,#ececec)}
.ashtray-photo{left:517px;top:1360px;width:683px;height:243px;background:radial-gradient(ellipse at 50% 60%,#ffffff 0%,#e9e9e9 40%,#dcdcdc 100%)}
.smoke-icon{left:118px;top:1430px}
.smoke-title{left:173px;top:1420px;font-family:"Exo 2",sans-serif;font-size:46px;font-weight:400;letter-spacing:1px;color:#333}
.smoke-title span{color:transparent;-webkit-text-stroke:1.5px var(--red)}
.smoke-text{left:121px;top:1484px;font-family:"Arimo",sans-serif;font-size:19px;color:#333}
.find-btn{left:118px;top:1518px;width:114px;height:28px;border-radius:14px;background:var(--yellow);border:2px solid #f7df8a;box-shadow:0 0 0 1px #d9a80c;font-family:"Arimo",sans-serif;font-size:10px;font-weight:700;color:#3a2c00;text-align:center;line-height:24px}

/* sponsors */
.sponsor-ribbon{left:497px;top:1646px}
.sponsor-ribbon-label{left:497px;top:1646px;width:206px;height:43px;line-height:43px;text-align:center;font-family:"Exo 2",sans-serif;font-size:21px;color:var(--white)}
.carousel-btn{top:1722px;width:29px;height:73px}
.carousel-btn.prev{left:114px;background:#e2e2e2}
.carousel-btn.next{left:1066px;background:var(--red)}
.sponsor-tile{top:1722px;height:73px;background:var(--white);border:1px solid #dcdcdc;display:flex;align-items:center;justify-content:center;font-family:"Questrial",sans-serif;font-size:15px;color:#333;text-align:center;line-height:17px}

/* footer */
.footer{left:0;top:1835px;width:1200px;height:379px;background:var(--footer-bg)}
.footer-heading{top:1892px;font-family:"Arimo",sans-serif;font-size:18px;color:var(--red);text-transform:uppercase}
.footer-rule{top:1926px;height:1px;background:var(--footer-line)}
.site-links{left:124px;top:1943px}
.site-links li{height:28px;line-height:28px;font-family:"Arimo",sans-serif;font-size:14px;color:var(--footer-text);padding-left:18px;position:relative}
.site-links li::before{content:"";position:absolute;left:0;top:11px;width:7px;height:7px;border:1.5px solid var(--footer-text)}
.site-links li.current{color:var(--yellow)}
.site-links li.current::before{border-color:var(--yellow)}
.news-arrow{top:1896px;width:16px;height:16px;border-radius:50%}
.news-item{left:393px}
.news-thumb{width:64px;height:47px;background:linear-gradient(135deg,#6b6b6b,#bdbdbd 50%,#4a5a3a)}
.news-copy{left:74px;top:-1px;width:210px;font-family:"Arimo",sans-serif;font-size:13px;line-height:14.5px;color:var(--white)}
.news-copy time{display:block;font-style:italic;font-size:11px;color:#8c8c8c;margin-top:2px}
.view-all{left:1018px;top:1896px;width:61px;height:16px;border-radius:8px;background:var(--yellow);font-family:"Arimo",sans-serif;font-size:9px;font-weight:700;color:#2a2000;text-align:center;line-height:16px}
.gallery-cell{}
.bottom-rule{left:120px;top:2158px;width:960px;height:1px;background:var(--footer-line)}
.copyright{left:120px;top:2180px;font-family:"Arimo",sans-serif;font-size:11px;color:#8c8c8c}
.social{top:2171px;width:26px;height:26px;border-radius:50%;border:1.5px solid #6a6a6a}
.social.first{border-color:#2e8fd6}
</style>
</head>
<body>

<!-- header -->
<div class="abs top-band"></div>
<div class="abs nav-bar"></div>
<a class="abs nav-link active">Home</a>
<a class="abs nav-link" style="left:239px">About Us</a>
<a class="abs nav-link" style="left:325px">News</a>
<a class="abs nav-link" style="left:389px">Fixture &amp; Results</a>
<div class="abs brand-tab">KESTONVALE<br>FC</div>
<a class="abs nav-link" style="left:686px">Photo Gallery</a>
<a class="abs nav-link" style="left:810px">Sponsor</a>
<a class="abs nav-link" style="left:894px">Club</a>
<a class="abs nav-link" style="left:950px">Contact Us</a>

<!-- hero -->
<div class="abs hero" role="img" aria-label="Young footballers mid-match in a floodlit stadium, one striking the ball while a keeper reaches out"></div>
<div class="abs hero-arrow prev">
  <svg width="38" height="38" viewBox="0 0 38 38"><path d="M21 13 L15 19 L21 25" fill="none" stroke="#fff" stroke-width="2"/></svg>
</div>
<div class="abs hero-arrow next">
  <svg width="38" height="38" viewBox="0 0 38 38"><path d="M17 13 L23 19 L17 25" fill="none" stroke="#c4161c" stroke-width="2"/></svg>
</div>
<div class="abs hero-badge"></div>
<h1 class="abs hero-title">KESTONVALE FC</h1>
<p class="abs hero-text">Lorem Ipsum is simply dummy text of the printing and typesetting industry. Lorem Ipsum has been the industry's standard dummy text .</p>

<!-- welcome -->
<div class="abs welcome" role="img" aria-label="Faded collage of smiling club members and supporters"></div>
<h2 class="abs welcome-title">WELCOME TO<span>KESTONVALE FC</span></h2>
<a class="abs register-btn"><span class="season">2014 Season</span><span class="cta">REGISTER ONLINE</span></a>
<h2 class="abs about-title">LET’S TALK <em>ABOUT</em> KESTONVALE FC.</h2>
<div class="abs about-rule"></div>
<p class="abs about-text">Lorem Ipsum is simply dummy text of the printing and typesetting industry. Lorem Ipsum has been the industry's standard dummy text ever since the 1500s, when an unknown printer took a galley of type and scrambled it to make a type specimen book. It has survived not only five centuries, but also the leap into electronic typesetting, remaining essentially unchanged. It was popularised in the 1960s with the release of Letraset sheets containing Lorem Ipsum passages.</p>

<!-- fixtures -->
<h2 class="abs fixtures-title">FIXTURES <span>&amp;</span> RESULTS</h2>
<div class="abs fixtures-rule"></div>
<p class="abs fixtures-text">Lorem Ipsum is simply dummy text of the printing and typesetting industry. Lorem Ipsum has been the industry's standard dummy text ever since the 1500s, when an unknown printer took a galley of type and scrambled it to make a type specimen book.</p>
<ul class="abs league-list" style="left:158px">
  <li>Premier League</li><li class="current">Premier League Res</li><li>Super League</li><li>Super League Res</li><li>Under 16 / 2</li><li>Under 17 / 1</li><li>Under 10 / 2</li><li>Under 10 / 3</li><li>Under 11 / 1</li><li>Under 12 / 3</li>
</ul>
<ul class="abs league-list" style="left:423px">
  <li>Under 13 / 3</li><li>Under 14 / 3</li><li>AA Men / 5</li><li>AA Men / 6</li><li>AA Men / 8</li><li>AA Men / 10</li><li>AA Men / 10</li><li>AA Men / 14</li><li>07 ECL / Red</li><li>07 ECL / Green</li>
</ul>
<ul class="abs league-list" style="left:643px">
  <li>07 ECL / Blue</li><li>08 ECL / Blue</li><li>08 ECL / Green</li><li>09 / Green</li><li>06 / A Green</li><li>06 / B Blue</li><li>06 / C Red</li><li>06 / D Purple</li><li>06 / E White</li><li>06 / F Brown</li>
</ul>
<div class="abs player-photo" role="img" aria-label="Footballer in a red kit standing with arms folded beside a ball"></div>

<!-- no smoking -->
<div class="abs smoke-band"></div>
<div class="abs ashtray-photo" role="img" aria-label="White ashtray surrounded by scattered cigarette butts and ash"></div>
<svg class="abs smoke-icon" width="37" height="37" viewBox="0 0 37 37">
  <circle cx="18.5" cy="18.5" r="16" fill="none" stroke="#c4161c" stroke-width="3"/>
  <rect x="9" y="16" width="19" height="5" fill="none" stroke="#c4161c" stroke-width="1.6"/>
  <line x1="7" y1="7" x2="30" y2="30" stroke="#c4161c" stroke-width="3"/>
</svg>
<h2 class="abs smoke-title">NO <span>SMOKING</span></h2>
<p class="abs smoke-text">There is a No Smoking Ban for all Sports Grounds</p>
<a class="abs find-btn">FIND OUT MORE</a>

<!-- sponsors -->
<svg class="abs sponsor-ribbon" width="206" height="43" viewBox="0 0 206 43">
  <path d="M12 0 H194 L206 21.5 L194 43 H12 L0 21.5 Z" fill="#c4161c"/>
</svg>
<h2 class="abs sponsor-ribbon-label">OUR SPONSORS</h2>
<div class="abs carousel-btn prev">
  <svg width="29" height="73" viewBox="0 0 29 73"><path d="M18 26 L11 36.5 L18 47" fill="none" stroke="#fff" stroke-width="2"/></svg>
</div>
<div class="abs sponsor-tile" style="left:149px;width:166px">Brightline Media</div>
<div class="abs sponsor-tile" style="left:324px;width:115px">Tallow</div>
<div class="abs sponsor-tile" style="left:466px;width:133px">Novacrest</div>
<div class="abs sponsor-tile" style="left:619px;width:169px">Harlan Pryce &amp; Co</div>
<div class="abs sponsor-tile" style="left:798px;width:148px">Corewell Seal</div>
<div class="abs sponsor-tile" style="left:956px;width:102px;font-size:12px;line-height:14px">Kestonvale<br>Bowling Club</div>
<div class="abs carousel-btn next">
  <svg width="29" height="73" viewBox="0 0 29 73"><path d="M11 26 L18 36.5 L11 47" fill="none" stroke="#fff" stroke-width="2"/></svg>
</div>

<!-- footer -->
<footer class="abs footer"></footer>

<h3 class="abs footer-heading" style="left:120px">Site Map</h3>
<div class="abs footer-rule" style="left:120px;width:201px"></div>
<ul class="abs site-links">
  <li>Become A Referee</li><li>News</li><li>Fixture &amp; Results</li><li class="current">Photo Gallery</li><li>Sponsor</li><li>Club</li><li>Contact Us</li>
</ul>

<h3 class="abs footer-heading" style="left:392px">Latest News</h3>
<svg class="abs news-arrow" style="left:675px" width="16" height="16" viewBox="0 0 16 16"><circle cx="8" cy="8" r="8" fill="#555"/><path d="M9.5 4.5 L6 8 L9.5 11.5" fill="none" stroke="#1d1d1d" stroke-width="1.6"/></svg>
<svg class="abs news-arrow" style="left:698px" width="16" height="16" viewBox="0 0 16 16"><circle cx="8" cy="8" r="8" fill="#f2c21b"/><path d="M6.5 4.5 L10 8 L6.5 11.5" fill="none" stroke="#1d1d1d" stroke-width="1.6"/></svg>
<div class="abs footer-rule" style="left:392px;width:325px"></div>
<article class="abs news-item" style="top:1954px">
  <div class="news-thumb" role="img" aria-label="Match action photo"></div>
  <p class="abs news-copy">Lorem Ipsum is simply dummy text of the typesetting industry.<time>Mar 11, 2014</time></p>
</article>
<article class="abs news-item" style="top:2019px">
  <div class="news-thumb" role="img" aria-label="Match action photo"></div>
  <p class="abs news-copy">Lorem Ipsum is simply dummy text of the typesetting industry.<time>Mar 11, 2014</time></p>
</article>
<article class="abs news-item" style="top:2084px">
  <div class="news-thumb" role="img" aria-label="Match action photo"></div>
  <p class="abs news-copy">Lorem Ipsum is simply dummy text of the typesetting industry.<time>Mar 11, 2014</time></p>
</article>

<h3 class="abs footer-heading" style="left:794px">Photo Gallery</h3>
<a class="abs view-all">VIEW ALL</a>
<div class="abs footer-rule" style="left:794px;width:285px"></div>
<div class="abs gallery-cell" style="left:797px;top:1951px;width:107px;height:111px;background:linear-gradient(160deg,#5a7fa8,#c1272d 60%,#6a1a1a)" role="img" aria-label="Junior player holding a medal"></div>
<div class="abs gallery-cell" style="left:909px;top:1951px;width:170px;height:62px;background:linear-gradient(160deg,#8a7a6a,#b59c82 50%,#4a4038)" role="img" aria-label="Group of club members"></div>
<div class="abs gallery-cell" style="left:909px;top:2017px;width:72px;height:64px;background:linear-gradient(160deg,#dcdcdc,#c1272d 70%)" role="img" aria-label="Player in red kit"></div>
<div class="abs gallery-cell" style="left:985px;top:2017px;width:94px;height:64px;background:linear-gradient(160deg,#3d5a2a,#e6e6e6 55%,#2f4a22)" role="img" aria-label="Junior team on the field"></div>
<div class="abs gallery-cell" style="left:797px;top:2066px;width:107px;height:64px;background:linear-gradient(160deg,#4f6b3a,#b92a2a 55%,#3a5028)" role="img" aria-label="Players lined up"></div>
<div class="abs gallery-cell" style="left:909px;top:2085px;width:72px;height:45px;background:linear-gradient(160deg,#7a8a6a,#e0e0e0 60%)" role="img" aria-label="Team celebration"></div>
<div class="abs gallery-cell" style="left:985px;top:2085px;width:94px;height:45px;background:linear-gradient(160deg,#5a7a44,#f0f0f0 50%,#c1272d)" role="img" aria-label="Team group photo"></div>

<div class="abs bottom-rule"></div>
<p class="abs copyright">Copyright .KESTONVALE FC ® 2014. All rights reserved. Terms and Conditions</p>
<div class="abs social first" style="left:917px" aria-label="Social link"></div>
<div class="abs social" style="left:950px" aria-label="Social link"></div>
<div class="abs social" style="left:984px" aria-label="Social link"></div>
<div class="abs social" style="left:1018px" aria-label="Social link"></div>
<div class="abs social" style="left:1051px" aria-label="Social link"></div>

</body>
</html>
```